Business Card Design

I'm looking for a cool business card design that showcases what my company does... I am the owner and Corvan is a play on my last name. The Corvan Group is a privately held entity that specializes in media (Corvan Media) and financial services (Corvan Trading).

Corvan Media focuses on the distribution and management of quality entertainment properties to all areas of the media world including broadcast, cable, digital, mobile and social media. Corvan Media helps media and entertainment companies create and market great content and ensure that it reaches the widest audience possible.

Corvan Media currently represents Glimmer TV (www.glimmertv-example.com), the fastest growing over the air broadcast network that focuses on programming that appeals to the African American audience. Corvan Media also represents two new over the air broadcast networks launching in Summer 2014 - Harbor TV (www.harbortv-example.com) and Plume TV (www.plumetv-example.com).

Corvan Media is an investor and business partner in SnapDrift (www.snapdrift-example.com) - a mobile social platform that empowers the user to choose how long your photos and videos live online.

Corvan Media also represents RMQ Enterprises (www.rmqent-example.com), an independent producer that creates talent-driven and cost-effective programming around emerging talent and Quillbright Content, a prolific producer of multimedia content including ZNK's hit program - Tundra Hall.

Corvan Trading manages a family office and focuses on building meaningful partnerships with all major financial institutions with a heavy concentration on IPO and secondary offerings.

Industry/Entity Type

Entertainment

Contact Information for Business Card

Marcus Pendle
12 Birchmere Lane
Roslyn New York 11592
O 555.201.0143
C 555.201.0178

```html
<!DOCTYPE html>
<html lang="en">
<head>
<meta charset="utf-8">
<title>The Corvan Group — Business Card</title>
<link rel="stylesheet" href="https://fonts.googleapis.com/css2?family=Arimo:wght@400;700&display=swap">
<style>
  :root {
    --stage: #ececec;
    --card: #ffffff;
    --slate: #76706a;
    --orange: #e0822a;
    --text-grey: #5f5a55;
    --moon: #efe6bf;
    --rule: #8a847e;
  }
  * { margin: 0; padding: 0; box-sizing: border-box; }
  html, body {
    width: 1200px; height: 900px; overflow: hidden;
    background: var(--stage);
    font-family: "Arimo", Arial, sans-serif;
  }
  .canvas {
    position: relative; width: 1200px; height: 900px;
    display: flex; align-items: center; justify-content: center;
  }
  .card {
    position: relative; width: 1000px; height: 572px;
    background: var(--card);
    box-shadow: 0 10px 30px rgba(0,0,0,0.18);
    overflow: hidden;
  }
  .top-tab {
    position: absolute; left: 0; top: 0;
    width: 610px; height: 38px;
    background: var(--slate);
    border-radius: 0 0 14px 0;
  }
  .brand {
    position: absolute; left: 100px; top: 226px;
    display: flex; align-items: center; gap: 20px;
  }
  .brand-dot {
    width: 96px; height: 96px; border-radius: 50%;
    background: var(--moon);
    flex: none;
  }
  .brand-name {
    font-weight: 700; font-size: 38px; line-height: 1.08;
    color: var(--slate); letter-spacing: 0.5px;
    white-space: nowrap;
  }
  .divider {
    position: absolute; left: 470px; top: 128px;
    width: 2px; height: 232px;
    background: var(--rule);
  }
  .contact {
    position: absolute; left: 520px; top: 132px;
  }
  .contact-name {
    color: var(--orange); font-weight: 700; font-size: 28px;
    letter-spacing: 0.5px; margin-bottom: 22px;
  }
  .phone {
    display: flex; align-items: center; gap: 14px;
    color: var(--text-grey); font-size: 27px; letter-spacing: 1px;
    margin-bottom: 6px;
  }
  .phone svg { width: 20px; height: 22px; flex: none; }
  .address {
    margin-top: 26px;
    color: var(--orange); font-weight: 700; font-size: 24px; line-height: 1.3;
  }
  .web-band {
    position: absolute; right: 0; bottom: 0;
    width: 440px; height: 84px;
    background: var(--orange);
    border-radius: 10px 0 0 0;
    display: flex; align-items: center; justify-content: center;
    color: #ffffff; font-weight: 700; font-size: 24px; letter-spacing: 0.3px;
  }
</style>
</head>
<body>
<main class="canvas">
  <section class="card" aria-label="Business card front">
    <div class="top-tab"></div>

    <div class="brand">
      <div class="brand-dot"></div>
      <div class="brand-name">The Corvan<br>Group</div>
    </div>

    <div class="divider"></div>

    <div class="contact">
      <p class="contact-name">MARCUS PENDLE</p>
      <p class="phone">
        <svg viewBox="0 0 24 24" aria-hidden="true"><path fill="var(--orange)" d="M6.6 10.8a15.1 15.1 0 0 0 6.6 6.6l2.2-2.2c.3-.3.7-.4 1-.2 1.1.4 2.3.6 3.6.6.6 0 1 .4 1 1V20c0 .6-.4 1-1 1A17 17 0 0 1 3 4c0-.6.4-1 1-1h3.5c.6 0 1 .4 1 1 0 1.3.2 2.5.6 3.6.1.3 0 .7-.2 1z"/></svg>
        555.201.0143
      </p>
      <p class="phone">
        <svg viewBox="0 0 24 24" aria-hidden="true"><rect x="6" y="2" width="12" height="20" rx="2" fill="var(--orange)"/><rect x="8" y="5" width="8" height="8" fill="#fff"/><rect x="8" y="15" width="2" height="2" fill="#fff"/><rect x="11" y="15" width="2" height="2" fill="#fff"/><rect x="14" y="15" width="2" height="2" fill="#fff"/></svg>
        555.201.0178
      </p>
      <p class="address">12 Birchmere Lane Ashcombe,<br>Westmark 04592</p>
    </div>

    <div class="web-band">www.thecorvangroup-example.com</div>
  </section>
</main>
</body>
</html>
```